Coach/consultant in conflict and challenge needs an enticing flyer

I need a double sided DL flyer design that will describe my work in helping people meet conflict and emotional challenge so they can learn and grow from these difficulties. I want to give a flavour of my style through fresh colours, repeated images used differently (the spiral), and a sense of positivity around conflict and difficulty. I want to attract people who are keen to do things differently and want to engage with creative processes rather than getting stuck in familiar patterns. My work is creative and often includes use of story, images and fables, so I want to convey that as well. I also place the work in a spiritual context, but grounded in practicality so I don't want it to seem New Age or flakey. I want something that seems innovative, professional and intriguing. I've included a sample of something I mocked up in word and also a copy of a flyer for Marla Quennet's Ember Gathering that inspired me to get a DL flyer. I want the design to communicate trust and transformation and engaging with fresh ways of doing things by moving past old habits

Target Market(s)

Mid 30s plus women and men who want to change their approach to conflict and emotional difficulties and are willing to take the creative and challenging journey to do that

Industry/Entity Type

Learn

Colors
acd136
00a990

Requirements
Must have
• a shift in the use of the spiral image,
• use of image of me (Norah)
• bright fresh colours olours that represent growth and transformation--I've suggested lime green as it suggests a sense of growth
• easy to read text
Nice to have
• Interesting non-traditional fonts perhaps text in a contemporary sans serif and another brush script font (like the Ember Gathering example)
• bleed to the edge and run off the page images or text
Should not have
• anything that represents too much tradition or stuckness

```html
<!DOCTYPE html>
<html lang="en">
<head>
<meta charset="utf-8">
<title>Norah Ellwyn – Coaching and Facilitation Flyer</title>
<link rel="stylesheet" href="https://fonts.googleapis.com/css2?family=Source+Sans+3:ital,wght@0,400;0,600;0,700;1,700&display=swap">
<style>
  :root {
    --lime: #acd136;
    --teal: #00a990;
    --ink: #333333;
    --ink-dark: #1f1f1f;
    --paper: #ffffff;
    --bar: #1a1a1a;
    --photo-a: #8e9aa6;
    --photo-b: #c9ccd0;
    --swirl: #ececec;
  }
  * { margin: 0; padding: 0; box-sizing: border-box; }
  html, body {
    width: 1200px; height: 2541px; overflow: hidden;
    background: var(--paper);
    font-family: "Source Sans 3", "Helvetica Neue", Arial, sans-serif;
    color: var(--ink);
  }
  .flyer { position: relative; width: 1200px; height: 2541px; overflow: hidden; background: var(--paper); }

  .hero-photo {
    position: absolute; left: 0; top: 0; width: 1200px; height: 860px;
    background: linear-gradient(135deg, var(--photo-b) 0%, var(--photo-a) 55%, #5d6d80 100%);
  }
  .swirl-area {
    position: absolute; border-radius: 50%;
    background: radial-gradient(circle, var(--swirl) 0%, rgba(236,236,236,0.5) 45%, rgba(255,255,255,0) 70%);
  }
  .swirl-left { left: -260px; top: 1380px; width: 760px; height: 760px; }
  .swirl-right { left: 520px; top: 700px; width: 900px; height: 900px; }

  .badge-image {
    position: absolute; left: 756px; top: 580px; width: 376px; height: 376px;
    border-radius: 50%; border: 12px solid var(--teal);
    background: radial-gradient(circle at 50% 40%, #e8f3fb 0%, #7fb6e0 60%, #3f7fb8 100%);
  }

  .intro {
    position: absolute; left: 52px; top: 1070px; width: 1100px;
    font-size: 33px; line-height: 46px; color: var(--ink);
  }
  .intro p + p { margin-top: 30px; }

  .services {
    position: absolute; left: 316px; top: 1645px; list-style: none;
  }
  .services li {
    display: flex; align-items: center; gap: 20px;
    font-size: 60px; line-height: 84px; color: var(--ink);
  }
  .services svg { width: 30px; height: 30px; flex: none; }

  .contact-band { position: absolute; left: 0; top: 1940px; width: 1200px; height: 480px; }

  .name {
    position: absolute; left: 40px; top: 2036px;
    font-size: 54px; font-weight: 700; font-style: italic; color: var(--ink-dark);
  }
  .credentials {
    position: absolute; left: 40px; top: 2104px;
    font-size: 28px; color: var(--ink-dark);
  }
  .phone-icon { position: absolute; left: 48px; top: 2196px; width: 48px; height: 48px; }
  .phones {
    position: absolute; left: 118px; top: 2188px;
    font-size: 31px; line-height: 40px; color: var(--ink-dark);
  }
  .mail-icon { position: absolute; left: 640px; top: 2200px; width: 52px; height: 36px; }
  .email {
    position: absolute; left: 708px; top: 2196px;
    font-size: 31px; line-height: 40px; color: var(--ink-dark);
  }
  .abn {
    position: absolute; left: 640px; top: 2242px;
    font-size: 31px; line-height: 40px; font-weight: 700; color: var(--ink-dark);
  }

  .web-bar {
    position: absolute; left: 0; top: 2420px; width: 1200px; height: 121px;
    background: var(--bar); color: var(--paper);
    display: flex; align-items: center; justify-content: center;
    font-size: 50px; font-weight: 400; letter-spacing: 1px;
  }
</style>
</head>
<body>
<main class="flyer">
  <div class="hero-photo" role="img" aria-label="Photo of a coaching session: a person taking notes on a clipboard facing a client"></div>

  <div class="swirl-area swirl-right" role="img" aria-label="Faint grey spiral decoration"></div>
  <div class="swirl-area swirl-left" role="img" aria-label="Faint grey spiral decoration"></div>

  <div class="badge-image" role="img" aria-label="Circular image of a road sign reading Positive Thinking with a smiley face"></div>

  <section class="intro">
    <p>Consult with Norah to address challenges in your life, relationship, group or organisation. Through listening, conversation and creative processes, you will discover what your challenge is asking of you. Norah Ellwyn is a skilled facilitator who works to shift people’s responses from reactivity to creativity.</p>
    <p>With many years’ experience in coaching and mentorship, mediation and narrative processes, Norah supports you to uncover unique responses to difficult situations.</p>
  </section>

  <ul class="services">
    <li><svg viewBox="0 0 24 24"><polygon fill="#00a990" points="12,1 15,9 23,9 16.5,14 19,22 12,17 5,22 7.5,14 1,9 9,9"/></svg>Consultations</li>
    <li><svg viewBox="0 0 24 24"><polygon fill="#00a990" points="12,1 15,9 23,9 16.5,14 19,22 12,17 5,22 7.5,14 1,9 9,9"/></svg>Workshops</li>
    <li><svg viewBox="0 0 24 24"><polygon fill="#00a990" points="12,1 15,9 23,9 16.5,14 19,22 12,17 5,22 7.5,14 1,9 9,9"/></svg>Speaking</li>
    <li><svg viewBox="0 0 24 24"><polygon fill="#00a990" points="12,1 15,9 23,9 16.5,14 19,22 12,17 5,22 7.5,14 1,9 9,9"/></svg>Articles</li>
  </ul>

  <svg class="contact-band" viewBox="0 0 1200 480" preserveAspectRatio="none" aria-hidden="true">
    <path d="M0 80 Q520 70 860 40 Q1060 20 1200 0 L1200 480 L0 480 Z" fill="#acd136"/>
  </svg>

  <div class="name">Norah Ellwyn</div>
  <div class="credentials">PhD, MCR, BAppSci, DipHum, AssDipEd</div>

  <svg class="phone-icon" viewBox="0 0 24 24" aria-hidden="true">
    <path fill="#1f1f1f" d="M6.6 10.8c1.4 2.8 3.8 5.1 6.6 6.6l2.2-2.2c.3-.3.7-.4 1-.2 1.1.4 2.3.6 3.6.6.6 0 1 .4 1 1V20c0 .6-.4 1-1 1C10.6 21 3 13.4 3 4c0-.6.4-1 1-1h3.5c.6 0 1 .4 1 1 0 1.3.2 2.5.6 3.6.1.3 0 .7-.2 1L6.6 10.8z"/>
  </svg>
  <div class="phones">0400 555 218 (m)<br>+61 3 9000 4417 (h)</div>

  <svg class="mail-icon" viewBox="0 0 26 18" aria-hidden="true">
    <rect x="0" y="0" width="26" height="18" fill="#ffffff"/>
    <path d="M0 0 L13 10 L26 0" fill="none" stroke="#acd136" stroke-width="1.6"/>
  </svg>
  <div class="email">norah@norahellwyn.com</div>
  <div class="abn">ABN 12 345 678 90</div>

  <footer class="web-bar">www.norahellwyn.com</footer>
</main>
</body>
</html>
```